依頼詳細
ロゴデータをご参考ください。
主に企業との挨拶時の利用になります。
ロゴカラーに沿うようなデザインでお願い致します。
記載項目
【会社名】ミナトコ株式会社
【役職】代表取締役会長
【名前】高森周平・SHUHEI TAKAMORI
【住所】〒650-0047 兵庫県神戸市中央区浜波通3-5-27
ソルナ東和ゲートビル9F
【電話・FAX】 TEL:078-392-4471 FAX:078-392-4472
【E-mail】takamori@minatoko-ex.ne.jp
【URL】http://www.minatoko-ex.jp
希望イメージ
シンプル 複雑
単色 カラフル
暗い 明るい
日常 高級
遊び心 厳粛
未来的 伝統的
女性的 男性的
希望する色
納品ファイル
• 高解像度JPG (.jpg)
• イラストレーター形式 (.ai)
• フォトショップ形式 (.psd)
• PNG形式 (.png)
補足説明
名刺の向きは縦・横どちらでも構いません。
大変申し訳ございませんでした。

ロゴデータの添付と、締め切りを
延長させて頂きました。

バランス具合の絶妙さ・色合い・・・
フィーリングで印象に残るようなデザインに
なっており、大変満足しております。

この度は、たくさんの素晴らしいデザインをご提案いただき、
誠にありがとうございました。
今後とも、各種ご依頼におきまして皆様の個性あふれる優れたアイデア
を以ってお力添えを頂ければと思います。

```html
<!DOCTYPE html>
<html lang="ja">
<head>
<meta charset="utf-8">
<title>ミナトコ株式会社 名刺</title>
<link rel="stylesheet" href="https://fonts.googleapis.com/css2?family=Noto+Sans+JP:wght@300;400;500&family=Noto+Serif+JP:wght@300;400&family=Cormorant+Garamond:ital,wght@1,400&display=swap">
<style>
  :root {
    --backdrop: #d9dadc;
    --card: #ffffff;
    --ink: #4a5560;
    --ink-soft: #6c7680;
    --rule: #b9c3cd;
    --brand: #1f5fae;
  }
  html, body {
    margin: 0;
    width: 893px;
    height: 1200px;
    overflow: hidden;
    background: var(--backdrop);
  }
  .card {
    position: absolute;
    left: 119px;
    top: 60px;
    width: 655px;
    height: 1080px;
    background: var(--card);
    overflow: hidden;
    font-family: "Noto Sans JP", sans-serif;
    color: var(--ink);
  }
  .card p, .card h1, .card address { margin: 0; }
  .role {
    position: absolute;
    top: 84px;
    width: 100%;
    text-align: center;
    font-size: 22px;
    line-height: 30px;
    font-weight: 300;
    letter-spacing: 0.08em;
  }
  .name {
    position: absolute;
    top: 126px;
    width: 100%;
    text-align: center;
    font-family: "Noto Serif JP", serif;
    font-size: 50px;
    line-height: 64px;
    font-weight: 300;
    letter-spacing: 0.18em;
    text-indent: 0.18em;
    color: var(--ink-soft);
  }
  .name-rule {
    position: absolute;
    top: 202px;
    left: 190px;
    width: 275px;
    height: 1px;
    background: var(--rule);
  }
  .name-roman {
    position: absolute;
    top: 212px;
    width: 100%;
    text-align: center;
    font-family: "Cormorant Garamond", serif;
    font-style: italic;
    font-size: 22px;
    line-height: 28px;
    letter-spacing: 0.06em;
    color: var(--ink-soft);
  }
  .brand-mark {
    position: absolute;
    top: 470px;
    width: 100%;
    display: flex;
    justify-content: center;
    align-items: center;
    gap: 18px;
  }
  .brand-mark .dot {
    width: 46px;
    height: 46px;
    border-radius: 50%;
    background: var(--brand);
  }
  .brand-mark .wordmark {
    font-size: 62px;
    font-weight: 500;
    letter-spacing: 0.04em;
    color: var(--brand);
    line-height: 1;
  }
  .company {
    position: absolute;
    top: 640px;
    width: 100%;
    text-align: center;
    font-size: 27px;
    line-height: 36px;
    font-weight: 400;
    letter-spacing: 0.06em;
    color: var(--brand);
  }
  .contact {
    position: absolute;
    top: 690px;
    left: 138px;
    font-size: 19px;
    font-weight: 300;
    line-height: 37px;
    color: var(--ink);
    font-style: normal;
  }
  .contact .gap { margin-left: 22px; }
  .band {
    position: absolute;
    left: 0;
    bottom: 0;
    width: 100%;
    height: 186px;
  }
  .url {
    position: absolute;
    right: 44px;
    bottom: 92px;
    font-size: 19px;
    line-height: 26px;
    font-weight: 300;
    color: var(--ink);
    letter-spacing: 0.03em;
  }
</style>
</head>
<body>
  <div class="card">
    <p class="role">代表取締役会長</p>
    <h1 class="name">高森周平</h1>
    <div class="name-rule"></div>
    <p class="name-roman">SHUHEI TAKAMORI</p>

    <div class="brand-mark">
      <span class="dot"></span>
      <span class="wordmark">MINATOKO</span>
    </div>

    <p class="company">ミナトコ株式会社</p>

    <address class="contact">
      〒650-0047<br>
      兵庫県神戸市中央区浜波通3-5-27<br>
      ソルナ東和ゲートビル9F<br>
      TEL 078-392-4471<span class="gap">FAX 078-392-4472</span><br>
      E-mail takamori@minatoko-ex.ne.jp
    </address>

    <svg class="band" viewBox="0 0 655 186" preserveAspectRatio="none" aria-hidden="true">
      <defs>
        <linearGradient id="bandBlue" x1="0" y1="0" x2="1" y2="0">
          <stop offset="0" stop-color="#0d3f85"/>
          <stop offset="0.55" stop-color="#2c74c6"/>
          <stop offset="1" stop-color="#8fb8e4"/>
        </linearGradient>
        <linearGradient id="bandPale" x1="0" y1="0" x2="1" y2="0">
          <stop offset="0" stop-color="#dde9f6"/>
          <stop offset="1" stop-color="#f6f9fd"/>
        </linearGradient>
      </defs>
      <path d="M0 14 C 200 0, 430 0, 655 10 L655 24 C 430 14, 200 16, 0 28 Z" fill="url(#bandBlue)"/>
      <rect x="0" y="34" width="655" height="78" fill="url(#bandPale)"/>
      <rect x="0" y="118" width="655" height="68" fill="url(#bandBlue)"/>
    </svg>
    <p class="url">http://www.minatoko-ex.jp</p>
  </div>
</body>
</html>
```